Etiketten für Imkerei
Zielgruppe
Wir sind eine Imkerei in München. Die Zielgrppe sind Menschen, die lokale Produkte wertschätzen, beim Produzenten gern direkt und auf Märkten einkaufen.
Hallo,
wir benötigen ein universelles Design für Honiggläser-Etiketten, das für verschiedene Sorten verwendet werden kann. Das vorhanden Logo soll im Design aufgenommen werden. Im Logo reicht der Name: Imkerei-Brunntal.

```html
<!DOCTYPE html>
<html lang="de">
<head>
<meta charset="utf-8">
<title>Etikett Waldhonig – Imkerei Brunntal</title>
<link rel="stylesheet" href="https://fonts.googleapis.com/css2?family=Parisienne&family=Source+Sans+3:wght@400;600&display=swap">
<style>
  :root {
    --honey: #ffcc00;
    --stripe-light: #d6d24a;
    --stripe-green: #c8c800;
    --ink: #111111;
    --white: #ffffff;
    --page: #ffffff;
  }
  html, body {
    margin: 0;
    padding: 0;
    width: 849px;
    height: 1200px;
    overflow: hidden;
    background: var(--page);
  }
  .canvas {
    position: relative;
    width: 849px;
    height: 1200px;
  }
  .label {
    position: absolute;
    left: 123px;
    top: 120px;
    width: 610px;
    height: 283px;
    background: var(--honey);
    overflow: hidden;
    font-family: "Source Sans 3", sans-serif;
  }
  .stripe {
    position: absolute;
    top: 0;
    height: 100%;
  }
  .stripe--light { background: var(--stripe-light); width: 38px; }
  .stripe--green { background: var(--stripe-green); width: 38px; }
  .front-stripe-a { left: 0; }
  .front-stripe-b { left: 38px; }
  .back-stripe-a { left: 333px; }
  .back-stripe-b { left: 371px; }

  .honeycomb {
    position: absolute;
    background: radial-gradient(ellipse at center, rgba(255,235,140,0.35), rgba(255,235,140,0) 70%);
  }
  .honeycomb--front { left: 0; top: 0; width: 330px; height: 230px; }
  .honeycomb--back { left: 300px; top: 0; width: 310px; height: 283px; }

  .grass {
    position: absolute;
    bottom: 0;
    height: 50px;
    background: linear-gradient(to top, rgba(200,200,0,0.35), rgba(200,200,0,0));
  }
  .grass--a { left: 55px; width: 60px; }
  .grass--b { left: 270px; width: 80px; }
  .grass--c { left: 480px; width: 100px; }

  .brand {
    position: absolute;
    left: 156px;
    top: 62px;
    width: 150px;
    text-align: center;
    font-weight: 600;
    font-size: 19px;
    color: var(--ink);
    line-height: 1.1;
  }
  .product-name {
    position: absolute;
    left: 128px;
    top: 166px;
    font-family: "Parisienne", cursive;
    font-size: 36px;
    color: var(--ink);
    margin: 0;
    font-weight: 400;
  }
  .weight {
    position: absolute;
    left: 17px;
    top: 249px;
    font-size: 12px;
    color: var(--white);
  }
  .description {
    position: absolute;
    right: 15px;
    top: 126px;
    width: 200px;
    text-align: right;
    color: var(--white);
    font-size: 9px;
    line-height: 11.4px;
  }
  .description__title {
    font-family: "Parisienne", cursive;
    font-size: 18px;
    line-height: 18px;
    display: block;
  }
  .description p { margin: 0; }
</style>
</head>
<body>
<div class="canvas">
  <section class="label" aria-label="Honigetikett Waldhonig">
    <div class="honeycomb honeycomb--front" role="img" aria-label="Wabenmuster als Hintergrund"></div>
    <div class="honeycomb honeycomb--back" role="img" aria-label="Wabenmuster als Hintergrund"></div>

    <div class="stripe stripe--light front-stripe-a"></div>
    <div class="stripe stripe--green front-stripe-b"></div>
    <div class="stripe stripe--light back-stripe-a"></div>
    <div class="stripe stripe--green back-stripe-b"></div>

    <div class="grass grass--a" role="img" aria-label="Gräser-Illustration"></div>
    <div class="grass grass--b" role="img" aria-label="Gräser-Illustration"></div>
    <div class="grass grass--c" role="img" aria-label="Gräser-Illustration"></div>

    <div class="brand">Imkerei Brunntal</div>
    <h1 class="product-name">Waldhonig</h1>
    <div class="weight">500 gr</div>

    <div class="description">
      <span class="description__title">Waldhonig,</span>
      <p>flüssig, 500 gr:</p>
      <p>Mit Beginn der Holunder-</p>
      <p>blüte ziehen die Völker in</p>
      <p>Waldgebiete um,</p>
      <p>um dort auf die Suche</p>
      <p>nach dem besonderen</p>
      <p>Waldhonig zu gehen.</p>
    </div>
  </section>
</div>
</body>
</html>
```